The Plaster & Resonance Craftworks Inc (PRCI)

Create a LOGO and Business Card design.

Colors: Black, Bright Yellow & Red

Description of company: commercial carpentry, metal framing, drywall, taping/spackling, demolition, rough/finish carpentry.

Target Market(s)

developers, architects, general contractors, construction managers

Industry/Entity Type

Business

```html
<!DOCTYPE html>
<html lang="en">
<head>
<meta charset="utf-8">
<title>Plaster &amp; Resonance Craftworks Inc — Business Card</title>
<link rel="stylesheet" href="https://fonts.googleapis.com/css2?family=Cinzel:wght@400&family=Jost:wght@400;600&display=swap">
<style>
  :root {
    --black: #050505;
    --charcoal: #2a2a2a;
    --red: #cc0a0a;
    --yellow: #fde43a;
    --ink: #0a0a0a;
  }
  html, body {
    margin: 0;
    padding: 0;
    width: 1200px;
    height: 677px;
    overflow: hidden;
    background: var(--black);
  }
  .card {
    position: relative;
    width: 1200px;
    height: 677px;
    overflow: hidden;
    background: radial-gradient(ellipse 60% 55% at 40% 30%, var(--charcoal) 0%, #151515 45%, var(--black) 100%);
  }
  .card__swoosh {
    position: absolute;
    inset: 0;
    width: 1200px;
    height: 677px;
  }
  .brand {
    position: absolute;
    left: 42px;
    top: 62px;
    display: flex;
    align-items: center;
    gap: 36px;
  }
  .brand__mark {
    width: 150px;
    height: 150px;
    background: var(--red);
  }
  .brand__name {
    margin: 0;
    font-family: "Jost", sans-serif;
    font-weight: 600;
    font-size: 44px;
    line-height: 1.25;
    color: var(--yellow);
  }
  .contact {
    position: absolute;
    right: 28px;
    top: 330px;
    text-align: right;
    color: var(--ink);
  }
  .contact__name {
    margin: 0;
    font-family: "Cinzel", serif;
    font-size: 76px;
    line-height: 1;
    letter-spacing: 5px;
  }
  .contact__phone {
    margin: 12px 0 0;
    font-family: "Cinzel", serif;
    font-size: 50px;
    line-height: 1;
    letter-spacing: 3px;
  }
  .contact__email {
    margin: 34px 0 0;
    font-family: "Jost", sans-serif;
    font-size: 37px;
    line-height: 1;
  }
  .contact__web {
    margin: 16px 0 0;
    font-family: "Jost", sans-serif;
    font-size: 56px;
    line-height: 1;
    letter-spacing: 1px;
  }
</style>
</head>
<body>
  <main class="card">
    <svg class="card__swoosh" viewBox="0 0 1200 677" aria-hidden="true">
      <path d="M218 677 Q520 200 1200 140 L1200 677 Z" fill="var(--yellow)"/>
      <path d="M250 677 Q545 225 1200 162 L1200 677 Z" fill="var(--red)"/>
    </svg>

    <header class="brand">
      <div class="brand__mark"></div>
      <p class="brand__name">Plaster &amp; Resonance<br>Craftworks Inc</p>
    </header>

    <section class="contact">
      <p class="contact__name">Daniel Harrow</p>
      <p class="contact__phone">Phone : 020 613 958</p>
      <p class="contact__email">Email : Info@plasterresonance.com</p>
      <p class="contact__web">www.plasterresonance.com</p>
    </section>
  </main>
</body>
</html>
```